Graphic- Educational Visual

Tandem Dog Training has created an educational tool to help its students understand and prioritize some key concepts in their dog training.

We are requesting a visual of this tool be designed.

Name/title of tool (to be included in graphic): The Tandem Compass
Description: Funnel (inverted pyramid).

From top to bottom, the levels are called:

Connect
Develop
Progress
Refine

The diagram should also include a cycle around it to, to represent that one is always moving through the levels.

Business colours are included below to make sure the funnel's colours complement the website colours or at least don't clash:

#0AA1C7 Blue and #7FC31B Green
Purple as a secondary colour -75279C

For reference, business logo is attached.

```html
<!DOCTYPE html>
<html lang="en">
<head>
<meta charset="utf-8">
<title>The Tandem Compass – Funnel</title>
<link href="https://fonts.googleapis.com/css2?family=Open+Sans:wght@300;400;700&display=swap" rel="stylesheet">
<style>
  :root {
    --brand-blue: #0AA1C7;
    --brand-green: #7FC31B;
    --paper: #ffffff;
    --ink-light: #ffffff;
  }
  html, body {
    margin: 0;
    padding: 0;
    overflow: hidden;
    background: var(--paper);
  }
  .sheet {
    position: relative;
    width: 1200px;
    height: 848px;
    overflow: hidden;
    background: var(--paper);
    font-family: "Open Sans", Arial, sans-serif;
  }
  .sheet svg { display: block; }
  .band-blue { fill: var(--brand-blue); }
  .band-green { fill: var(--brand-green); }
  .sheet-title, .sheet-label {
    fill: var(--ink-light);
    font-weight: 300;
  }
  .sheet-title { font-size: 30px; }
  .sheet-label { font-size: 28px; }
  .brand-name {
    fill: var(--brand-blue);
    font-weight: 700;
  }
  .funnel-tier { fill: var(--brand-blue); }
  .tier-label {
    fill: var(--ink-light);
    font-size: 26px;
    font-weight: 300;
    letter-spacing: 0.5px;
  }
  .tier-icon { fill: var(--ink-light); stroke: none; }
  .tier-icon-line { fill: none; stroke: var(--ink-light); stroke-width: 1.6; }
</style>
</head>
<body>
<main class="sheet">
  <svg width="1200" height="848" viewBox="0 0 1200 848" xmlns="http://www.w3.org/2000/svg">
    <!-- header bands -->
    <polygon class="band-blue" points="0,0 1200,0 1200,32 724,32 700,54 0,54"/>
    <polygon class="band-green" points="0,54 458,54 436,78 0,78"/>
    <text class="sheet-title" x="29" y="39">The Tandem Compass</text>

    <!-- brand name -->
    <g class="brand">
      <text class="brand-name" x="1120" y="118" text-anchor="end" font-size="64">Tandem</text>
      <text class="brand-name" x="1120" y="160" text-anchor="end" font-size="27">Dog Training</text>
    </g>

    <!-- funnel tiers -->
    <g class="funnel">
      <polygon class="funnel-tier" points="366,198 833,198 784,297 416,297"/>
      <polygon class="funnel-tier" points="417,303 783,303 734,406 466,406"/>
      <polygon class="funnel-tier" points="468,412 732,412 682,514 518,514"/>
      <polygon class="funnel-tier" points="520,520 681,520 603,672 597,672"/>

      <!-- connect icon -->
      <g class="icon-connect">
        <polyline class="tier-icon-line" points="600,222 585,239 615,239 600,222"/>
        <circle class="tier-icon" cx="600" cy="222" r="3.5"/>
        <circle class="tier-icon" cx="585" cy="239" r="3.5"/>
        <circle class="tier-icon" cx="615" cy="239" r="3.5"/>
      </g>
      <text class="tier-label" x="600" y="277" text-anchor="middle">CONNECT</text>

      <!-- develop icon -->
      <g class="icon-develop">
        <circle class="tier-icon" cx="591" cy="330" r="7"/>
        <circle fill="var(--brand-blue)" cx="591" cy="330" r="2.5"/>
        <circle class="tier-icon-line" cx="610" cy="341" r="6"/>
        <circle class="tier-icon-line" cx="610" cy="341" r="2"/>
        <circle class="tier-icon" cx="595" cy="350" r="5"/>
        <circle fill="var(--brand-blue)" cx="595" cy="350" r="1.8"/>
      </g>
      <text class="tier-label" x="600" y="386" text-anchor="middle">DEVELOP</text>

      <!-- progress icon -->
      <g class="icon-progress">
        <rect class="tier-icon" x="583" y="447" width="9" height="10"/>
        <rect class="tier-icon-line" x="595" y="441" width="9" height="16"/>
        <rect class="tier-icon" x="607" y="435" width="9" height="22"/>
        <path class="tier-icon-line" d="M583 440 Q598 430 614 428"/>
        <polygon class="tier-icon" points="617,424 610,425 614,431"/>
      </g>
      <text class="tier-label" x="600" y="489" text-anchor="middle">PROGRESS</text>

      <!-- refine icon -->
      <g class="icon-refine">
        <polygon class="tier-icon-line" points="587,532 613,532 603,546 603,558 597,554 597,546"/>
      </g>
      <text class="tier-label" x="600" y="590" text-anchor="middle">REFINE</text>
    </g>

    <!-- footer bands -->
    <polygon class="band-green" points="742,792 766,768 1200,768 1200,792"/>
    <polygon class="band-blue" points="0,816 477,816 500,792 1200,792 1200,848 0,848"/>
    <text class="sheet-label" x="1174" y="832" text-anchor="end">Funnel</text>
  </svg>
</main>
</body>
</html>
```